School Hallway Magnetic Display Design for school values

I am looking for a someone to help me design a magnetic hallway display that will hang in the hallway of our small school. There are several elements, including 1. 6ft by 4ft designed magnetic bulletin board, 2. Magnets that will stick to the board. See attachment for which elements belong where. The display will be for our TRAVEK program, which rewards students for demonstrating our school values. We want the display to be beautiful and interactive. We are also rebranding, so we want the design to align with our new fonts and colors. In the attached PDF is an outline of our new brand guidelines. Unfortunately, we don't have the color codes, but I'm hoping that you can match the colors listed. Attached are elements to be used on the board, but please use your creativity to make it more dynamic and visually appealing. For example, the star magnets could be another shape. The TRAVEK magnets must remain the same. I've included two photos of boards at other schools that inspired this project.

Target Market(s)

School Community

Industry/Entity Type

Education

Requirements
Should not have
• School Logo

```html
<!DOCTYPE html>
<html lang="en">
<head>
<meta charset="utf-8">
<title>TRAVEK of the Month – Hallway Values Board</title>
<link rel="stylesheet" href="https://fonts.googleapis.com/css2?family=Merriweather:ital,wght@0,700;0,900;1,700&display=swap">
<style>
  :root {
    --forest: #1f5230;
    --forest-deep: #184426;
    --leaf: #4f8b3d;
    --fern: #6ea53a;
    --lime: #b6c72b;
    --citron: #d2d63a;
    --sky: #97b6d9;
    --board: #f1f2f2;
    --panel: #fbfbfb;
    --ghost: #e6e8e7;
    --ink: #1d2a22;
    --white: #ffffff;
  }
  * { box-sizing: border-box; margin: 0; padding: 0; }
  html, body { width: 890px; height: 1200px; overflow: hidden; }
  body { background: var(--board); font-family: "Merriweather", Georgia, serif; color: var(--ink); }

  .board {
    position: relative; width: 890px; height: 1200px;
    background: linear-gradient(160deg, #f7f8f8 0%, var(--board) 55%, #eceeed 100%);
  }
  .title-band {
    position: absolute; left: 12px; right: 12px; top: 60px; height: 142px;
    background: var(--forest);
    display: flex; align-items: center; justify-content: center;
  }
  .title-band h1 {
    color: var(--white); font-style: italic; font-weight: 700;
    font-size: 72px; letter-spacing: 0.5px;
  }
  .feature-panel {
    position: absolute; left: 47px; top: 245px; width: 422px; height: 571px;
    background: var(--panel);
  }
  .compass-mark {
    position: absolute; left: 533px; top: 817px; width: 340px; height: 340px;
    border-radius: 50%; background: radial-gradient(circle, #eef0ef 0%, var(--ghost) 100%);
  }

  .thermometer { position: absolute; left: 488px; top: 236px; }
  .thermo-scale {
    position: absolute; left: 561px; top: 268px;
    list-style: none; color: var(--leaf); font-size: 17px; font-weight: 700;
  }
  .thermo-scale li { height: 46.2px; line-height: 24px; }

  .value-list { position: absolute; left: 618px; top: 246px; list-style: none; }
  .value-tag {
    width: 248px; height: 78px; margin-bottom: 17px;
    background: var(--white); border: 4px solid var(--fern); border-radius: 6px;
    box-shadow: inset 0 0 0 3px var(--white), inset 0 0 0 5px var(--fern);
    display: flex; align-items: center; justify-content: center;
    font-size: 32px; font-weight: 700; color: var(--ink);
  }
  .value-tag.dark { border-color: var(--forest); box-shadow: inset 0 0 0 3px var(--white), inset 0 0 0 5px var(--forest); }

  .magnets-label {
    position: absolute; left: 0; width: 560px; top: 836px;
    text-align: center; font-size: 21px; font-weight: 900;
  }
  .magnet-grid {
    position: absolute; left: 50px; top: 872px;
    display: grid; grid-template-columns: repeat(4, 90px); column-gap: 17px; row-gap: 6px;
  }
  .magnet { width: 90px; height: 90px; display: block; }
</style>
</head>
<body>
<main class="board">
  <header class="title-band"><h1>TRAVEK of the Month</h1></header>

  <section class="feature-panel" aria-label="Featured students"></section>

  <div class="compass-mark" role="img" aria-label="Faint compass rose decoration"></div>

  <svg class="thermometer" width="84" height="570" viewBox="0 0 84 570" aria-label="Progress thermometer">
    <defs>
      <linearGradient id="mercury" x1="0" y1="0" x2="0" y2="1">
        <stop offset="0" stop-color="#dedc3e"/>
        <stop offset="0.4" stop-color="#8fb23a"/>
        <stop offset="0.75" stop-color="#3d7a36"/>
        <stop offset="1" stop-color="#1f5230"/>
      </linearGradient>
    </defs>
    <rect x="22" y="4" width="40" height="500" rx="20" fill="#111" />
    <circle cx="42" cy="524" r="40" fill="#111"/>
    <rect x="27" y="9" width="30" height="500" rx="15" fill="#fff"/>
    <circle cx="42" cy="524" r="35" fill="#fff"/>
    <rect x="31" y="14" width="22" height="500" rx="11" fill="url(#mercury)"/>
    <circle cx="42" cy="524" r="31" fill="var(--forest)"/>
    <g stroke="#1a1a1a" stroke-width="2">
      <line x1="42" y1="78" x2="53" y2="78"/><line x1="42" y1="124" x2="53" y2="124"/>
      <line x1="42" y1="170" x2="53" y2="170"/><line x1="42" y1="216" x2="53" y2="216"/>
      <line x1="42" y1="262" x2="53" y2="262"/><line x1="42" y1="308" x2="53" y2="308"/>
      <line x1="42" y1="354" x2="53" y2="354"/><line x1="42" y1="400" x2="53" y2="400"/>
      <line x1="42" y1="446" x2="53" y2="446"/>
    </g>
  </svg>
  <ol class="thermo-scale">
    <li>100%</li><li>90%</li><li>80%</li><li>70%</li><li>60%</li><li>50%</li>
    <li>30%</li><li>20%</li><li>10%</li><li>0%</li>
  </ol>

  <ul class="value-list">
    <li class="value-tag">Simplicity</li>
    <li class="value-tag dark">Peace</li>
    <li class="value-tag">Integrity</li>
    <li class="value-tag">Community</li>
    <li class="value-tag dark">Equality</li>
    <li class="value-tag">Stewardship</li>
  </ul>

  <h2 class="magnets-label">Achievement Magnets</h2>
  <div class="magnet-grid">
    <svg class="magnet" viewBox="0 0 100 100"><polygon points="50,4 62,37 97,38 69,59 79,94 50,73 21,94 31,59 3,38 38,37" fill="var(--leaf)" stroke="#3b6e2d" stroke-width="3" stroke-linejoin="round"/></svg>
    <svg class="magnet" viewBox="0 0 100 100"><polygon points="50,4 62,37 97,38 69,59 79,94 50,73 21,94 31,59 3,38 38,37" fill="var(--citron)" stroke="#a9ad24" stroke-width="3" stroke-linejoin="round"/></svg>
    <svg class="magnet" viewBox="0 0 100 100"><polygon points="50,4 62,37 97,38 69,59 79,94 50,73 21,94 31,59 3,38 38,37" fill="var(--sky)" stroke="#7496bd" stroke-width="3" stroke-linejoin="round"/></svg>
    <svg class="magnet" viewBox="0 0 100 100"><circle cx="50" cy="50" r="45" fill="var(--fern)" stroke="#4f8130" stroke-width="3"/><circle cx="50" cy="50" r="37" fill="none" stroke="#fff" stroke-width="3"/></svg>

    <svg class="magnet" viewBox="0 0 100 100"><polygon points="50,4 62,37 97,38 69,59 79,94 50,73 21,94 31,59 3,38 38,37" fill="var(--lime)" stroke="#8f9d20" stroke-width="3" stroke-linejoin="round"/></svg>
    <svg class="magnet" viewBox="0 0 100 100"><circle cx="50" cy="50" r="45" fill="var(--sky)" stroke="#7496bd" stroke-width="3"/><circle cx="50" cy="50" r="37" fill="none" stroke="#fff" stroke-width="3"/></svg>
    <svg class="magnet" viewBox="0 0 100 100"><circle cx="50" cy="50" r="45" fill="var(--forest)" stroke="var(--forest-deep)" stroke-width="3"/><circle cx="50" cy="50" r="37" fill="none" stroke="#fff" stroke-width="3"/></svg>
    <svg class="magnet" viewBox="0 0 100 100"><circle cx="50" cy="50" r="45" fill="var(--citron)" stroke="#a9ad24" stroke-width="3"/><circle cx="50" cy="50" r="37" fill="none" stroke="#fff" stroke-width="3"/></svg>

    <svg class="magnet" viewBox="0 0 100 100"><polygon points="50,4 62,37 97,38 69,59 79,94 50,73 21,94 31,59 3,38 38,37" fill="var(--forest)" stroke="var(--forest-deep)" stroke-width="3" stroke-linejoin="round"/></svg>
    <svg class="magnet" viewBox="0 0 100 100"><polygon points="50,4 62,37 97,38 69,59 79,94 50,73 21,94 31,59 3,38 38,37" fill="var(--fern)" stroke="#4f8130" stroke-width="3" stroke-linejoin="round"/></svg>
    <svg class="magnet" viewBox="0 0 100 100"><polygon points="50,4 62,37 97,38 69,59 79,94 50,73 21,94 31,59 3,38 38,37" fill="var(--leaf)" stroke="#3b6e2d" stroke-width="3" stroke-linejoin="round"/></svg>
    <svg class="magnet" viewBox="0 0 100 100"><circle cx="50" cy="50" r="45" fill="var(--sky)" stroke="#7496bd" stroke-width="3"/><circle cx="50" cy="50" r="37" fill="none" stroke="#fff" stroke-width="3"/></svg>
  </div>
</main>
</body>
</html>
```